Business Card Design Project

Please create a custom business card for Loftwell Capital. The logo is attached to this brief.

Also, here is the link to the logo design project: http://jobs.briskmotif.com/job.aspx?id=462035

Questions can be posted on the Discussion Board.

```html
<!DOCTYPE html>
<html lang="en">
<head>
<meta charset="utf-8">
<title>Loftwell Capital – Business Card</title>
<link rel="stylesheet" href="https://fonts.googleapis.com/css2?family=Ubuntu:wght@400;500;700&display=swap">
<style>
  :root {
    --backdrop: #d9d9d6;
    --card-grey: #6a6a6a;
    --card-black: #121212;
    --ink-white: #f2f2f2;
    --ink-soft: #e4e4e4;
    --brand-blue: #1f4fa8;
    --brand-blue-light: #3d7fd6;
    --logo-silver: #cfcfcf;
  }
  * { box-sizing: border-box; margin: 0; padding: 0; }
  html, body {
    width: 1200px; height: 873px; overflow: hidden;
    background: var(--backdrop);
    font-family: "Ubuntu", sans-serif;
  }
  .sheet {
    width: 1200px; height: 873px;
    display: flex; align-items: center; justify-content: center; gap: 60px;
  }
  .card {
    width: 520px; height: 297px; position: relative;
    border-radius: 4px;
    box-shadow: 0 10px 28px rgba(0,0,0,.22);
    overflow: hidden;
  }
  /* Front */
  .card--front { background: var(--card-grey); color: var(--ink-white); }
  .front__brand {
    position: absolute; left: 44px; top: 70px;
    display: flex; flex-direction: column; align-items: flex-start; gap: 10px;
  }
  .brand-mark { width: 26px; height: 26px; background: var(--brand-blue-light); }
  .brand-name {
    font-weight: 500; color: var(--ink-white);
    letter-spacing: 3px; text-transform: uppercase; line-height: 1.15;
  }
  .front__brand .brand-name { font-size: 26px; }
  .front__divider {
    position: absolute; left: 262px; top: 40px; width: 2px; height: 217px;
    background: linear-gradient(to bottom, rgba(61,127,214,0), var(--brand-blue-light) 50%, rgba(61,127,214,0));
  }
  .front__details { position: absolute; left: 290px; top: 48px; width: 215px; }
  .person-name { font-size: 21px; font-weight: 700; color: var(--brand-blue); }
  .person-title { font-size: 13px; color: var(--ink-soft); margin-top: 3px; }
  .address { font-size: 13px; line-height: 1.45; color: var(--ink-soft); margin-top: 14px; }
  .contact-list { list-style: none; margin-top: 14px; }
  .contact-list li {
    display: flex; align-items: center; gap: 8px;
    font-size: 13px; line-height: 1.65; color: var(--ink-soft);
  }
  .contact-list svg { width: 11px; height: 11px; flex: none; fill: var(--brand-blue-light); }
  /* Back */
  .card--back { background: var(--card-black); display: flex; align-items: center; justify-content: center; }
  .back__brand { display: flex; align-items: center; gap: 14px; }
  .back__brand .brand-mark { background: var(--logo-silver); width: 30px; height: 30px; }
  .back__brand .brand-name { font-size: 30px; color: var(--logo-silver); }
</style>
</head>
<body>
<main class="sheet">
  <section class="card card--front" aria-label="Business card front">
    <div class="front__brand">
      <span class="brand-mark"></span>
      <span class="brand-name">Loftwell<br>Capital</span>
    </div>
    <div class="front__divider"></div>
    <div class="front__details">
      <p class="person-name">Daniel Moreau</p>
      <p class="person-title">Managing Director</p>
      <p class="address">Unit 4, Harbor Row,<br>Easton, State 60917</p>
      <ul class="contact-list">
        <li><svg viewBox="0 0 12 12"><path d="M2.5 0.5l2 2.2-1 1.3c.7 1.6 2 2.9 3.5 3.6l1.3-1 2.2 2-1.1 2.2C5 10.6 1.4 7 .4 1.6z"/></svg>+481 555 0142</li>
        <li><svg viewBox="0 0 12 12"><rect x="1" y="3" width="10" height="7" rx="1"/><rect x="3" y="0.5" width="6" height="3"/></svg>+481 555 0187</li>
        <li><svg viewBox="0 0 12 12"><path d="M0.5 2.5h11v7h-11z M0.5 2.5l5.5 4 5.5-4" /></svg>daniel@loftwellcapital.com</li>
        <li><svg viewBox="0 0 12 12"><circle cx="6" cy="6" r="5.5"/></svg>www.loftwellcapital.com</li>
      </ul>
    </div>
  </section>

  <section class="card card--back" aria-label="Business card back">
    <div class="back__brand">
      <span class="brand-mark"></span>
      <span class="brand-name">Loftwell Capital</span>
    </div>
  </section>
</main>
</body>
</html>
```